Lantern Crest Gathering Day 2021

I am looking to create a flyer for a one day prayer retreat our church is organizing. This flyer will be posted on social media, websites, mobile apps, and will also be printed so it can be mailed to people.

I am looking for something professional, with good use of our logo and band colors (logo colors).

I am counting on the designer's skill, creativity, art and knowledge of media communication to produce a flyer that will effectively and quickly convey the message we are trying to spread.

CONTENT OF THE FLYER:
Event title: Lantern Crest Gathering Day
Date: Tuesday July 2nd, 2021
Time: 11:00AM - 7:00PM
Brindlewick Hotel, 4817 Fennimore Street, Portland, Maine 04102 (Room: Thistlemoor)
Event Key words to highlight what the event is about: Prayer, Fasting, Worship, Prophecy, Revival.
Key phrases:
A one day prayer retreat.
Jesus Chris is Lord

Contact info:
www.velunto.org
Phone: 207 555 0143
Email: contact@quillbrookfold.org

```html
<!DOCTYPE html>
<html lang="en">
<head>
<meta charset="utf-8">
<title>Lantern Crest Gathering Day 2021</title>
<link rel="stylesheet" href="https://fonts.googleapis.com/css2?family=Exo+2:ital,wght@1,900&family=Montserrat:wght@600;700&family=Teko:wght@500&display=swap">
<style>
  :root {
    --stage: #ececec;
    --night: #2a3a86;
    --midnight: #222f70;
    --glow: #6a82d0;
    --sea: #1f6cb4;
    --crowd: #10284d;
    --wood: rgba(176, 146, 108, 0.75);
    --wood-soft: rgba(140, 112, 80, 0.35);
    --dove: rgba(235, 240, 255, 0.5);
    --white: #ffffff;
    --gold: #ffd21a;
    --rule: rgba(255, 255, 255, 0.85);
  }
  * { box-sizing: border-box; margin: 0; padding: 0; }
  html, body { width: 1199px; height: 1200px; overflow: hidden; }
  body { background: var(--stage); position: relative; }

  .flyer {
    position: absolute; left: 152px; top: 20px;
    width: 895px; height: 1160px; overflow: hidden;
    color: var(--white);
    font-family: "Montserrat", Arial, sans-serif;
  }
  .flyer__backdrop {
    position: absolute; inset: 0;
    background:
      radial-gradient(ellipse 50% 32% at 50% 42%, var(--glow) 0%, transparent 70%),
      radial-gradient(ellipse 70% 25% at 50% 100%, var(--crowd) 0%, transparent 80%),
      linear-gradient(180deg, var(--midnight) 0%, var(--night) 30%, #2d4f9e 58%, var(--sea) 78%, #174f8c 100%);
  }
  .dove { position: absolute; top: 0; width: 250px; height: 200px;
    background: radial-gradient(ellipse 50% 45% at 50% 45%, var(--dove) 0%, transparent 75%); }
  .dove--left { left: 0; }
  .dove--right { right: 0; }

  .cross { position: absolute; top: 160px; width: 270px; height: 720px; }
  .cross--left { left: 0;
    background:
      radial-gradient(ellipse 45% 30% at 45% 28%, var(--wood) 0%, transparent 80%),
      radial-gradient(ellipse 30% 55% at 30% 55%, var(--wood-soft) 0%, transparent 85%); }
  .cross--right { right: 0;
    background:
      radial-gradient(ellipse 45% 30% at 55% 28%, var(--wood) 0%, transparent 80%),
      radial-gradient(ellipse 30% 55% at 70% 55%, var(--wood-soft) 0%, transparent 85%); }

  .brand { position: absolute; top: 100px; left: 0; right: 0; text-align: center;
    font-weight: 600; font-size: 52px; letter-spacing: 2px; color: var(--white); }

  .keywords, .tagline { position: absolute; left: 0; right: 0; text-align: center;
    font-family: "Teko", "Arial Narrow", sans-serif; font-weight: 500;
    color: var(--gold); letter-spacing: 0.5px; }
  .keywords { top: 232px; font-size: 30px; }
  .tagline { top: 752px; font-size: 28px; }

  .title { position: absolute; top: 282px; left: 0; right: 0; text-align: center;
    font-family: "Exo 2", Impact, sans-serif; font-weight: 900; font-style: italic;
    text-transform: uppercase; line-height: 1; letter-spacing: -1px;
    text-shadow: 0 0 18px rgba(255, 255, 255, 0.35); }
  .title__line { display: block; font-size: 104px; margin-bottom: 30px; }
  .title__line--wide { font-size: 88px; letter-spacing: -2px; margin-top: 6px; }

  .rule { position: absolute; left: 27px; right: 27px; height: 2px; background: var(--rule); }
  .rule--top { top: 726px; }
  .rule--mid { top: 804px; }
  .rule--bottom { top: 1122px; }
  .rule--dashed { top: 904px; height: 0; background: none; border-top: 2px dashed var(--rule); }

  .when { position: absolute; top: 856px; left: 0; right: 0; height: 34px;
    font-weight: 700; font-size: 27px; }
  .when__date { position: absolute; left: 65px; }
  .when__time { position: absolute; left: 511px; }
  .when__divider { position: absolute; left: 461px; top: -4px; height: 42px;
    border-left: 2px dashed var(--rule); }

  .venue { position: absolute; top: 948px; left: 0; right: 0; text-align: center;
    font-weight: 700; font-size: 31px; line-height: 42px; }
  .venue__room { display: block; margin-top: 14px; font-size: 36px; color: var(--gold); }
</style>
</head>
<body>
  <main class="flyer">
    <div class="flyer__backdrop" role="img" aria-label="Worship crowd with raised hands under blue stage lights"></div>
    <div class="dove dove--left" role="img" aria-label="White dove in flight"></div>
    <div class="dove dove--right" role="img" aria-label="White dove in flight"></div>
    <div class="cross cross--left" role="img" aria-label="Weathered wooden cross leaning in from the left"></div>
    <div class="cross cross--right" role="img" aria-label="Weathered wooden cross leaning in from the right"></div>

    <div class="brand">VELUNTO</div>

    <p class="keywords">PRAYER, FASTING, WORSHIP, PROPHECY, REVIVAL</p>

    <h1 class="title">
      <span class="title__line">Lantern</span>
      <span class="title__line">Crest</span>
      <span class="title__line title__line--wide">Gathering Day</span>
    </h1>

    <div class="rule rule--top"></div>
    <p class="tagline">A ONE DAY PRAYER RETREAT. JESUS CHRIS IS LORD</p>
    <div class="rule rule--mid"></div>

    <div class="when">
      <span class="when__date">TUESDAY JULY 2nd, 2021</span>
      <span class="when__divider"></span>
      <span class="when__time">11:00 a.m. - 7:00 p.m.</span>
    </div>
    <div class="rule rule--dashed"></div>

    <p class="venue">
      BRINDLEWICK HOTEL, 4817 FENNIMORE STREET,<br>
      PORTLAND, MAINE 04102
      <span class="venue__room">(ROOM : THISTLEMOOR)</span>
    </p>

    <div class="rule rule--bottom"></div>
  </main>
</body>
</html>
```